Modern Small Law Firm Website To Look Cutting Edge

I need a website design for a new, single-attorney law firm. The firm will be called "The Ashcombe Law Group." Our goal is to handle car accident and general personal injury lawsuits for individuals.

Our selling points are: (1) We charge less so you keep more; (2) We have experience and success trying and settling multi-million dollar cases; (3) We use modern technology to make the whole process simple, easy and hassle-free for clients.

Also because we are a one-man law firm, the clients will personally know the lawyer and have access to them. For that reason, I thought a good big tagline for the website would be "KNOW YOUR LAWYER"

I like the idea of splitting the website vertically down the middle, with the left side having a blue background, a picture of me, and big white lettering for the tagline, and the right side having a white background with blue lettering and headlines. I don't want navy blue or royal blue, but a more bright and eye-catching blue color. We can experiment with different shades.

I would be curious about how it could look with some minor orange accent coloring somewhere.

I need to feature prominently, probably in the top left corner, this phone number: 504-271-9038.

This will be used as much by mobile users as it would be by desktop/computer users.

The final design should communicate trust, convenience and cutting edge technology that leads to success.

Finally, I would be curious how we can have a sleek looking info submission box somewhere on the right side nearer the bottom that features different combinations of presenting these phrases: "QUICK QUESTION? QUICK ANSWER" The info submission button could say "Ask"

I am uploading two different pictures of me that can be used. The gray backgrounds are not necessary or good, if there is a way to cut them out that would be great. I can try and get that if needed.

Target Market(s)

Individuals who have been hurt by others, mostly in car accidents. They will be frustrated, inconvenienced and need to be soothed.

Industry/Entity Type

Legal

Number of Pages Required

1 page

Font styles to use
Sans Serif

Colors
0692cd
33a6d7
85cae6
faa54b
f78f20
3276b5

Requirements
Must have
• If you have started designing already, please note that the project description information is more important than the image that I uploaded originally. It has since been deleted.
• Also please now use the color photo that has been uploaded.
Nice to have
• I really want a clean and simple website design with not a lot of clutter. I'd like to avoid the typical law firm websites that you see that have tool bars across the top and basic borders/columns everywhere. It needs to grab your attention and look a little more cutting edge and different.
• Let's experiment with different eye-catching ways to present the three value propositions I noted.
• Also if the screen is split vertically with the left and right side being blue and white, maybe we can experiment with different ways that the two colors could fade into each other as opposed to just a line where one color starts and the other ends.
• And maybe the blue/white backgrounds could be textured somehow so that they don't appear flat. Perhaps we could try using differing shades of blue to give the appearance of pattern or 3D texture.
Should not have
• The basic picture/design I uploaded is just a suggestion, but there isn't really anything there.

```html
<!DOCTYPE html>
<html lang="en">
<head>
<meta charset="utf-8">
<title>The Ashcombe Law Group</title>
<link rel="stylesheet" href="https://fonts.googleapis.com/css2?family=PT+Sans:ital,wght@0,400;0,700;1,400&display=swap">
<style>
  :root {
    --sky: #0aa2cc;
    --sky-light: #1ab0d8;
    --ink: #10364a;
    --royal: #3276b5;
    --cyan: #0aa3cb;
    --powder: #72b8d8;
    --orange: #f78f20;
    --peach: #f2c08a;
    --white: #ffffff;
    --label: #6b6b6b;
    --phone: #1b8fd0;
  }
  * { margin: 0; padding: 0; box-sizing: border-box; }
  html, body { width: 1200px; height: 900px; overflow: hidden; background: var(--white); }
  body { font-family: "PT Sans", sans-serif; position: relative; }

  .hero {
    position: absolute; left: 0; top: 0; width: 730px; height: 900px;
    background: radial-gradient(circle at 265px 250px, var(--sky-light) 0%, var(--sky) 70%);
  }
  .brand {
    position: absolute; left: 67px; top: 38px;
    color: var(--white); font-weight: 700; font-size: 29px; letter-spacing: 0.3px;
  }
  .portrait {
    position: absolute; left: 99px; top: 188px; width: 359px; height: 485px;
    background: linear-gradient(180deg, #8a8a8a 0%, #3a3a3a 45%, #222 100%);
    border-radius: 120px 120px 0 0;
  }
  .tagline {
    position: absolute; left: 0; top: 673px; width: 722px; height: 227px;
    background: var(--ink); color: var(--white);
  }
  .tagline .lead { position: absolute; left: 93px; top: 42px; font-size: 29px; font-weight: 700; white-space: nowrap; }
  .tagline .big { position: absolute; left: 91px; top: 68px; font-size: 76px; font-weight: 700; letter-spacing: -0.5px; white-space: nowrap; }
  .accent { color: var(--orange); }

  .contact {
    position: absolute; left: 840px; top: 42px; display: flex; align-items: center; gap: 12px;
    color: var(--phone); font-style: italic; font-size: 33px;
  }

  .value { position: absolute; color: var(--white); }
  .value h2 { font-size: 18px; font-weight: 700; margin-bottom: 6px; }
  .value p { font-size: 13.5px; line-height: 1.4; }
  .value-price { left: 730px; top: 121px; width: 234px; height: 194px; background: var(--royal); padding: 70px 0 0 16px; }
  .value-price p { width: 210px; }
  .value-easy { left: 968px; top: 121px; width: 232px; height: 194px; background: var(--cyan); padding: 64px 0 0 25px; }
  .value-easy p { width: 175px; }
  .value-big { left: 730px; top: 318px; width: 470px; height: 164px; background: var(--powder); text-align: center; padding-top: 30px; }
  .value-big h2 { margin-bottom: 10px; }

  .ask-title {
    position: absolute; left: 818px; top: 519px; width: 274px; text-align: center;
    font-size: 24px; font-weight: 700; color: var(--cyan);
  }
  .splash {
    position: absolute; left: 880px; top: 568px; width: 203px; height: 270px;
    background: var(--orange); border-radius: 40px;
  }
  .ask-form { position: absolute; left: 818px; top: 575px; width: 274px; }
  .field {
    display: block; width: 274px; height: 34px; margin-bottom: 10px;
    background: var(--peach); border: 0; padding: 0 16px;
    font-family: "PT Sans", sans-serif; font-size: 14px; color: var(--label);
  }
  .field::placeholder { color: var(--label); }
  .field-message { height: 120px; padding-top: 12px; resize: none; }
  .ask-btn {
    display: block; width: 120px; height: 43px; margin-top: 3px; border: 0; border-radius: 3px;
    background: var(--orange); color: var(--white);
    font-family: "PT Sans", sans-serif; font-weight: 700; font-size: 22px;
  }
</style>
</head>
<body>
  <section class="hero">
    <div class="brand">ASHCOMBE LAW GROUP</div>
    <div class="portrait" role="img" aria-label="Portrait of the attorney in a dark suit and striped tie"></div>
    <div class="tagline">
      <p class="lead">Car Wreck? <span class="accent">Know Your Lawyer.</span></p>
      <p class="big">We <span class="accent">Can</span> Help.</p>
    </div>
  </section>

  <div class="contact">
    <svg width="12" height="20" viewBox="0 0 12 20" aria-hidden="true">
      <rect x="1" y="3" width="10" height="16" rx="1.5" fill="none" stroke="#333" stroke-width="1.5"/>
      <rect x="3" y="5.5" width="6" height="5" fill="#333"/>
      <line x1="9" y1="0" x2="9" y2="3" stroke="#333" stroke-width="1.5"/>
    </svg>
    <span>504-271-9038</span>
  </div>

  <article class="value value-price">
    <h2>Never More Than 24%</h2>
    <p>We charge less than others, so you keep more.</p>
  </article>
  <article class="value value-easy">
    <h2>We Make It Easy</h2>
    <p>Modern tools keep your case simple and hassle-free.</p>
  </article>
  <article class="value value-big">
    <h2>Big Firm Lawyering</h2>
    <p>With experience in multi-million dollar<br>litigation, we get results.</p>
  </article>

  <h3 class="ask-title">Quick <span class="accent">Question ?</span></h3>
  <div class="splash" role="img" aria-label="Orange paint splash accent behind the form"></div>
  <form class="ask-form">
    <input class="field" type="text" placeholder="Name">
    <input class="field" type="tel" placeholder="Phone">
    <input class="field" type="email" placeholder="Email">
    <textarea class="field field-message" placeholder="Your Message"></textarea>
    <button class="ask-btn" type="button">ASK</button>
  </form>
</body>
</html>
```